Creative Businesss Card desgin!

Create a business card for our business Glint window cleaning!
We are open to creative ideas as long as it maintains a professional image.

Target Market(s)

Small Commercial window cleaning clients including car dealerships, strata manager, cafe

Industry/Entity Type

Window Cleaning

Contact Information for Business Card

Darren Pilkey
General Manager
Glint Window Cleaning

darren@glintservices.com.au
pane-tidy-corner.com.au
Ph: 1800 GO GLINT
Mob: 0438 572 619

Colors
fbed22
0392cd

Requirements
Should not have
• Stock window cleaning/ squeegee graphics

```html
<!DOCTYPE html>
<html lang="en">
<head>
<meta charset="utf-8">
<title>Glint Window Cleaning — Business Card</title>
<link href="https://fonts.googleapis.com/css2?family=Montserrat:wght@700&family=Work+Sans:wght@400;800&display=swap" rel="stylesheet">
<style>
  :root {
    --page: #1e1e1e;
    --card-blue: #11598b;
    --card-blue-light: #1a6594;
    --brand-yellow: #f7ef24;
    --text-white: #ffffff;
  }
  * { box-sizing: border-box; margin: 0; padding: 0; }
  html, body {
    width: 1200px; height: 900px; overflow: hidden;
    background: var(--page);
  }
  .sheet {
    position: relative; width: 1200px; height: 900px;
    display: flex; flex-direction: column; align-items: center;
    justify-content: center; gap: 40px;
  }
  .card {
    position: relative; width: 700px; height: 400px;
    background: linear-gradient(135deg, var(--card-blue) 0%, var(--card-blue-light) 55%, var(--card-blue) 100%);
    border-bottom: 7px solid var(--brand-yellow);
    font-family: "Work Sans", sans-serif;
    color: var(--text-white);
  }
  .brand-name {
    font-family: "Work Sans", sans-serif;
    font-weight: 800;
    color: var(--brand-yellow);
    line-height: 1;
    white-space: nowrap;
  }

  /* Front */
  .card--front { display: flex; flex-direction: column; align-items: center; }
  .card--front .brand-name { margin-top: 165px; font-size: 48px; letter-spacing: 1px; }
  .card__url {
    position: absolute; bottom: 22px; left: 0; right: 0;
    text-align: center; font-size: 16px; letter-spacing: 0.8px;
  }

  /* Back */
  .card--back { display: flex; align-items: center; padding-left: 40px; }
  .card--back .brand-name { font-size: 22px; }
  .divider {
    width: 2px; height: 165px; background: var(--brand-yellow);
    margin: 0 30px 0 24px; flex: none;
  }
  .contact__name {
    font-family: "Montserrat", sans-serif; font-weight: 700;
    font-size: 25px; letter-spacing: 3px; color: var(--brand-yellow);
    text-transform: uppercase; white-space: nowrap;
  }
  .contact__role { font-size: 16px; letter-spacing: 1.2px; margin-top: 2px; }
  .contact__list { list-style: none; margin-top: 18px; }
  .contact__item {
    display: flex; align-items: center; gap: 9px; white-space: nowrap;
    font-size: 16px; letter-spacing: 0.6px; line-height: 24px;
  }
  .contact__icon { width: 13px; height: 13px; flex: none; }
</style>
</head>
<body>
<main class="sheet">
  <section class="card card--front">
    <p class="brand-name">Glint Window Cleaning</p>
    <p class="card__url">pane-tidy-corner.com.au</p>
  </section>

  <section class="card card--back">
    <p class="brand-name">Glint Window Cleaning</p>
    <div class="divider"></div>
    <div class="contact">
      <h1 class="contact__name">Darren Pilkey</h1>
      <p class="contact__role">General Manager</p>
      <ul class="contact__list">
        <li class="contact__item">
          <svg class="contact__icon" viewBox="0 0 16 16" fill="none" stroke="#f7ef24" stroke-width="1.6"><path d="M4 1.5 6.5 5 5 6.5c.8 1.8 2.4 3.4 4.5 4.5L11 9.5l3.5 2.5-1.5 2.5C7.5 14 2 8.5 1.5 3z"/></svg>
          <span>1800 GO GLINT</span>
        </li>
        <li class="contact__item">
          <svg class="contact__icon" viewBox="0 0 16 16" fill="none" stroke="#f7ef24" stroke-width="1.6"><rect x="4" y="1" width="8" height="14" rx="1.5"/><line x1="7" y1="12.5" x2="9" y2="12.5"/></svg>
          <span>0438 572 619</span>
        </li>
        <li class="contact__item">
          <svg class="contact__icon" viewBox="0 0 16 16" fill="none" stroke="#f7ef24" stroke-width="1.6"><rect x="1" y="3" width="14" height="10"/><path d="M1 3l7 6 7-6"/></svg>
          <span>darren@glintservices.com.au</span>
        </li>
        <li class="contact__item">
          <svg class="contact__icon" viewBox="0 0 16 16" fill="none" stroke="#f7ef24" stroke-width="1.4"><circle cx="8" cy="8" r="6.5"/><ellipse cx="8" cy="8" rx="3" ry="6.5"/><line x1="1.5" y1="8" x2="14.5" y2="8"/></svg>
          <span>pane-tidy-corner.com.au</span>
        </li>
      </ul>
    </div>
  </section>
</main>
</body>
</html>
```